Vela Errands Web Design Project

Homepage components
o Logo
o Rotating header
o Main menu
o Animation video
o Banners
o Members login
o Latest news

The design’s preferred colors are black (background), silver (main tabs) and white (text)

Site map:
• Home
• News
• About us
o Welcome Note
o Company Profile
• Member Log in
o Registered homepage
? Request a service (form)
? Services directory
? Update profile
? Services history
• Member registration
o Registration form
• Partners
Footer Menu
• Contact us
• Terms & Conditions
• Privacy policy
• Social media links
• Sitemap

Brief about the company:
Vela Errands is a Jordanian company dedicated to elevate and redefine the level of service in the country. We are set out to give premium services at affordable prices. In this fast paced environment that we live in, we barely have the luxury of free time anymore and we, at Vela Errands will be giving you that extra hour or two per day to spend as your heart desires!
By becoming a member you will get access to a world of comfort and peace of mind. We have done the homework on your behalf and have established the network of connections that will enable you to live a headache free life.
We will be providing our members with support and assistance in their day to day lives in the fields that consumes and wastes time the most. We are value driven and below is our “ever-growing” list of services that we will provide at excellent prices:
• Maintenance (carpentry, plumbing, electrical, painting, decorating, gardening… etc)
• Cleaning (pre and post tenancy, periodical deep cleaning, packing and moving services, laundry… etc)
• Personalized delivery services (grocery, important documents, office related supplies, posting cheques, food, paying bills… etc)
• Passport, driving license and ID reissuance
• Travel arrangements (flights, hotels, airport transfers… etc)
• Premium car rental services
• Restaurant reservations
• IT assistance
• Event planning and all related services
• Catering arrangements

Aside from all the services we have on offer we have collaborated with a number of places (that we like to call partners) in town where Vela Errands members are entitled to benefits and privileges that will most certainly add value to their membership. Alongside our partners we have come up with the best formula that will please our members. Below are some of our current partners:

Requirements
Must have
• Homepage components
o Logo
o Rotating header
o Main menu
o Animation video
o Banners
o Members login
o Latest news

```html
<!DOCTYPE html>
<html lang="en">
<head>
<meta charset="utf-8">
<title>Vela Errands</title>
<link rel="stylesheet" href="https://fonts.googleapis.com/css2?family=Pinyon+Script&family=Tinos:wght@400&family=Arimo:wght@400;700&display=swap">
<style>
:root{
  --page:#0b0b0b;
  --header:#ececec;
  --ink:#1c1c1c;
  --white:#ffffff;
  --silver:#a9a9a9;
  --muted:#9a9a9a;
  --rule:#2c2c2c;
  --panel:#1e1e1e;
  --video:#1f2024;
}
*{box-sizing:border-box;margin:0;padding:0}
html,body{width:930px;height:1200px;overflow:hidden}
body{position:relative;background:var(--page);font-family:"Arimo",Arial,sans-serif;color:var(--white)}
.abs{position:absolute}
.script{font-family:"Pinyon Script",cursive;font-weight:400}

/* header */
.site-header{left:0;top:0;width:930px;height:127px;background:linear-gradient(#f2f2f2,#e4e4e4)}
.brand{left:128px;top:22px}
.brand-name{font-family:"Pinyon Script",cursive;font-size:44px;color:var(--ink);line-height:1}
.brand-tag{font-size:12px;color:#8a8a8a;margin:2px 0 0 30px;letter-spacing:.3px}
.login{left:498px;top:13px;display:flex;align-items:center;gap:5px}
.login-label{font-family:"Tinos",serif;font-size:11px;color:var(--ink);margin-right:9px}
.login-field{width:86px;height:20px;background:#a5a8aa;border:1px solid #c5c7c8;font-size:8px;color:#dfe1e2;padding:4px 6px}
.login-btn{width:46px;height:20px;background:linear-gradient(#d8d8d8,#9b9b9b);border:1px solid #7c7c7c;font-size:10px;color:#111;display:flex;align-items:center;justify-content:center}

/* nav */
.main-nav{left:0;top:127px;width:930px;height:38px;background:linear-gradient(#4a4a4a,#1c1c1c 55%,#0f0f0f);border-top:1px solid #6a6a6a}
.main-nav span{position:absolute;top:11px;font-size:10.5px;color:#e8e8e8}
.nav-marker{left:181px;top:127px;width:0;height:0;border-left:5px solid transparent;border-right:5px solid transparent;border-top:6px solid #f0f0f0}

/* hero */
.hero{left:0;top:165px;width:930px;height:287px;background:radial-gradient(ellipse at 50% 30%,#b8b8b8,#8f8f8f 60%,#6c6c6c);border-bottom:1px solid #5a5a5a}
.hero-title{left:128px;top:192px;font-size:32px;color:var(--white);text-shadow:0 1px 3px rgba(0,0,0,.35)}
.hero-text{left:128px;top:254px;width:366px;font-family:"Tinos",serif;font-size:14px;line-height:18.2px;color:var(--white)}
.hero-card{left:512px;top:200px;width:285px;height:170px;border-radius:10px;transform:rotate(-14deg);background:linear-gradient(135deg,#4a4a4a,#1b1b1b 60%,#2a2a2a);box-shadow:0 6px 14px rgba(0,0,0,.45)}
.hero-dots{left:420px;top:431px;display:flex;gap:3px}
.hero-dots i{width:11px;height:11px;border-radius:50%;background:radial-gradient(circle at 40% 35%,#fff,#bcbcbc);display:block}
.hero-dots i.on{background:radial-gradient(circle at 40% 35%,#666,#111);border:1px solid #999}

/* news */
.news-bar{left:119px;top:467px;width:688px;height:50px;background:linear-gradient(#262626,#181818);border:1px solid #555}
.news-title{left:9px;top:8px;font-size:24px;color:#ddd}
.news-divider{left:130px;top:3px;width:1px;height:42px;background:#3a3a3a}
.news-text{left:162px;top:18px;font-size:10px;color:#eee}

/* section headings */
.section-title{font-size:27px;color:#e6e6e6;line-height:1}
.section-rule{height:1px;background:var(--rule)}
.copy{font-size:10px;line-height:14px;color:#eaeaea}

.video{left:119px;top:569px;width:325px;height:198px;background:var(--video)}
.video-play{left:153px;top:63px}
.video-label{left:0;top:93px;width:325px;text-align:center;font-family:"Tinos",serif;font-size:21px;color:var(--white)}
.video-bar{left:0;top:178px;width:325px;height:20px;background:linear-gradient(#2a2a2a,#111);border-top:2px solid #333}
.video-progress{left:0;top:-2px;width:32px;height:2px;background:#c0261f}
.video-time{left:70px;top:5px;font-size:8px;color:#ddd}
.video-time em{font-style:normal;color:#888}

.photo{left:581px;top:830px;width:225px;height:134px;border:2px solid #e4e4e4;background:linear-gradient(120deg,#8c8c8c,#cfcfcf 55%,#f1f1f1)}
.service-thumb{top:1022px;width:108px;height:70px;border:1px solid #ddd;background:linear-gradient(#d9d9d9,#8f8f8f)}
.more{left:720px;top:1106px;font-size:8.5px;color:#fff;display:flex;align-items:center;gap:4px}

/* footer */
.footer-rule{left:0;top:1143px;width:930px;height:1px;background:#262626}
.footer-links{left:129px;top:1162px;font-size:8.5px;color:#ddd;word-spacing:1px}
.footer-copy{left:129px;top:1176px;font-size:7.5px;color:#888}
.follow{left:703px;top:1163px;font-size:8.5px;color:#ddd}
.social{top:1159px;width:15px;height:15px;background:#f2f2f2}
</style>
</head>
<body>

<header class="abs site-header">
  <div class="abs brand">
    <div class="brand-name">Vela Errands</div>
    <div class="brand-tag">errands done for you</div>
  </div>
  <form class="abs login">
    <span class="login-label">Member Login</span>
    <span class="login-field">User Id</span>
    <span class="login-field">••••••••••••••</span>
    <span class="login-btn">Login</span>
  </form>
</header>

<nav class="abs main-nav">
  <span style="left:173px">Home</span>
  <span style="left:277px">About Us</span>
  <span style="left:395px">News</span>
  <span style="left:497px">Member Log in</span>
  <span style="left:642px">Member Registration</span>
</nav>
<div class="abs nav-marker"></div>

<section class="abs hero"></section>
<h1 class="abs script hero-title">Welcome to Vela Errands</h1>
<p class="abs hero-text">We are a Jordanian company that will be offering premium services to our members in various fields. In return we will be charging a nominal annual membership fee obtained from those interested in our services. We will be issuing a membership card for each member and we are due to launch our services mid June, 2012.</p>
<div class="abs hero-card" role="img" aria-label="Dark membership card with the company name and member details"></div>
<div class="abs hero-dots"><i class="on"></i><i></i><i></i><i></i><i></i><i></i><i></i></div>

<section class="abs news-bar">
  <h2 class="abs script news-title">Our News</h2>
  <div class="abs news-divider"></div>
  <p class="abs news-text">We have a strong team of dedicated tele-concierge agents that will receive calls from 8am – 2am, 7 days a week.</p>
</section>

<h2 class="abs script section-title" style="left:456px;top:527px">Why Vela Errands</h2>
<div class="abs section-rule" style="left:456px;top:558px;width:344px"></div>
<p class="abs copy" style="left:457px;top:568px;width:345px">In addition to offering premium services at low costs, our cardholders will also gain from our partnerships with various restaurants, hotels, florists, spas, beauty centers and selected retail shops through value programs and promotions.</p>
<p class="abs copy" style="left:457px;top:652px;width:345px">We expect that an active user should save a considerable amount of money through such partnerships which will reflect instant value to the members. We have in excess of 50 contracted venues as part of our network and we are looking to increase that to around 100 by end of 2012.</p>

<div class="abs video">
  <svg class="abs video-play" width="21" height="21" viewBox="0 0 21 21" aria-hidden="true">
    <circle cx="10.5" cy="10.5" r="10" fill="#2f7fd6" stroke="#cfe3fa"/>
    <path d="M8 6 L15 10.5 L8 15 Z" fill="#fff"/>
  </svg>
  <div class="abs video-label">Animation Video</div>
  <div class="abs video-bar">
    <div class="abs video-progress"></div>
    <svg class="abs" style="left:16px;top:5px" width="60" height="10" aria-hidden="true">
      <rect x="0" y="0" width="2.5" height="9" fill="#ccc"/><rect x="5" y="0" width="2.5" height="9" fill="#ccc"/>
      <path d="M30 3 H33 L37 0 V9 L33 6 H30 Z" fill="#aaa"/>
    </svg>
    <span class="abs video-time">0:14 <em>/ 4:05</em></span>
    <svg class="abs" style="left:212px;top:4px" width="108" height="12" aria-hidden="true">
      <rect x="0" y="2" width="11" height="8" rx="2" fill="none" stroke="#999"/>
      <circle cx="27" cy="6" r="4" fill="#999"/>
      <circle cx="47" cy="6" r="4.5" fill="#999"/>
      <rect x="65" y="3" width="11" height="6" fill="none" stroke="#999"/>
      <rect x="83" y="2" width="12" height="8" fill="none" stroke="#ccc"/>
      <path d="M99 1h3M99 1v3M108 1h-3M108 1v3M99 11h3M99 11v-3M108 11h-3M108 11v-3" stroke="#ccc"/>
    </svg>
  </div>
</div>

<h2 class="abs script section-title" style="left:119px;top:790px">How Will We Operate</h2>
<div class="abs section-rule" style="left:119px;top:822px;width:681px"></div>
<p class="abs copy" style="left:119px;top:832px;width:445px">We have a strong team of dedicated tele-concierge agents that will receive calls from 8am – 2am, 7 days a week (to become 24/7 when needed). All of our requests will be handled through our dedicated concierge line (+962-6-555-0142) or website, which is currently under construction (www.velaerrands.jo).</p>
<p class="abs copy" style="left:119px;top:903px;width:445px">We at Vela Errands will ensure that each request will be given the utmost attention and will be handled as if it was our only request. A tracing system is in place for proper follow up to take place before, during and after any request is made.</p>
<div class="abs photo" role="img" aria-label="Black and white photo of call centre agents wearing headsets"></div>

<h2 class="abs script section-title" style="left:124px;top:975px">Our Services</h2>
<div class="abs section-rule" style="left:119px;top:1006px;width:684px"></div>
<div class="abs service-thumb" style="left:121px" role="img" aria-label="Passport and travel documents"></div>
<div class="abs service-thumb" style="left:236px" role="img" aria-label="Airplane at a tropical resort"></div>
<div class="abs service-thumb" style="left:351px" role="img" aria-label="Rental car"></div>
<div class="abs service-thumb" style="left:466px" role="img" aria-label="Diners at a restaurant table"></div>
<div class="abs service-thumb" style="left:581px;background:linear-gradient(#ffffff,#d6d6d6)" role="img" aria-label="Computer equipment for IT assistance"></div>
<div class="abs service-thumb" style="left:696px" role="img" aria-label="Row of piggy banks"></div>
<div class="abs more">View More Services
  <svg width="5" height="7" aria-hidden="true"><path d="M0 0 L5 3.5 L0 7 Z" fill="#fff"/></svg>
</div>

<footer>
  <div class="abs footer-rule"></div>
  <div class="abs footer-links">Contact Us &nbsp;|&nbsp; Terms &amp; Conditions &nbsp;|&nbsp; Privacy Policy &nbsp;|&nbsp; Sitemap</div>
  <div class="abs footer-copy">© 2012, All Rights Reserved</div>
  <div class="abs follow">Follow Us</div>
  <div class="abs social" style="left:754px" aria-label="Social link"></div>
  <div class="abs social" style="left:779px" aria-label="Social link"></div>
</footer>

</body>
</html>
```